Visitenkarten-Design für Styling-Coach
Zielgruppe
Styling Coach
Aufgabenstellung
Colors, Logo, Two side design, one side with Information/Logo other backside nice design
Info Card Front:
Helene Sofia Krantz
Lindenhof 27
8847 Talberg
krantz@krantzstyling.example
www.krantzstyling.example

```html
<!DOCTYPE html>
<html lang="de">
<head>
<meta charset="utf-8">
<title>Visitenkarte – Helene Sofia Krantz, Styling Coach</title>
<link rel="stylesheet" href="https://fonts.googleapis.com/css2?family=Open+Sans:wght@400;600;700&display=swap">
<style>
  :root {
    --page-bg: #ecebe8;
    --card-pink: #f2bcd3;
    --card-lilac: #dcd6e6;
    --card-blue: #c4e3f5;
    --ink: #3f3f3f;
    --accent-pink: #d9569d;
    --mark-faint: rgba(255, 255, 255, 0.45);
    --shadow: rgba(0, 0, 0, 0.14);
  }
  * { box-sizing: border-box; margin: 0; padding: 0; }
  html, body {
    width: 1200px;
    height: 900px;
    overflow: hidden;
    background: var(--page-bg);
    font-family: "Open Sans", Arial, sans-serif;
    color: var(--ink);
  }
  .sheet {
    width: 1200px;
    height: 900px;
    display: flex;
    flex-direction: column;
    align-items: center;
    justify-content: center;
    gap: 26px;
  }
  .card {
    position: relative;
    width: 640px;
    height: 414px;
    background: linear-gradient(90deg, var(--card-pink) 0%, var(--card-lilac) 45%, var(--card-blue) 100%);
    box-shadow: 0 6px 18px var(--shadow);
    overflow: hidden;
  }

  /* Logo side */
  .brand {
    position: absolute;
    left: 70px;
    top: 150px;
  }
  .brand-line {
    display: flex;
    align-items: center;
    gap: 14px;
  }
  .brand-dot {
    width: 22px;
    height: 22px;
    border-radius: 50%;
    background: var(--accent-pink);
  }
  .brand-name {
    font-weight: 400;
    font-size: 36px;
    letter-spacing: 2px;
    text-transform: uppercase;
    color: var(--ink);
  }
  .brand-tagline {
    margin-top: 14px;
    font-weight: 400;
    font-size: 36px;
    letter-spacing: 15px;
    text-transform: uppercase;
    color: var(--ink);
  }

  /* Info side */
  .info-mark {
    position: absolute;
    right: 40px;
    top: 30px;
    width: 290px;
    height: 290px;
    border-radius: 50%;
    background: var(--mark-faint);
  }
  .contact {
    position: absolute;
    left: 60px;
    top: 130px;
    font-size: 22px;
    line-height: 1.2;
  }
  .contact-name {
    font-weight: 700;
    font-size: 23px;
    letter-spacing: 0.6px;
    margin-bottom: 12px;
  }
  .contact-block { margin-bottom: 12px; }
  .contact-email { letter-spacing: 0.4px; }
  .website {
    position: absolute;
    right: 44px;
    bottom: 46px;
    font-weight: 700;
    font-size: 23px;
    letter-spacing: 0.8px;
  }
</style>
</head>
<body>
<main class="sheet">

  <section class="card card-logo" aria-label="Vorderseite mit Namenszug">
    <div class="brand">
      <div class="brand-line">
        <span class="brand-name">Helene Sofia Krantz</span>
        <span class="brand-dot" aria-hidden="true"></span>
      </div>
      <div class="brand-tagline">Styling Coach</div>
    </div>
  </section>

  <section class="card card-info" aria-label="Rückseite mit Kontaktdaten">
    <div class="info-mark" aria-hidden="true"></div>
    <address class="contact" style="font-style: normal;">
      <p class="contact-name">Helene Sofia Krantz</p>
      <p class="contact-block">Lindenhof 27<br>8847 Talberg</p>
      <p class="contact-block">+41 44 555 0192<br>+41 79 555 0147</p>
      <p class="contact-email">krantz@krantzstyling.example</p>
    </address>
    <p class="website">www.krantzstyling.example</p>
  </section>

</main>
</body>
</html>
```